Marlow Vane Lettings Web Site Design

I am after a very simple 3 page web site please. I attach a PDF with the text and information. The logo is also in the PDF. The colours should be orange and blues. The pages should be HOME - LANDLORDS - TENANTS.
Lettings and Property Management Company aimed at just being a reference point for tenants but more of a sales pitch to landlords. Please refer to the attached PDF and word file which contains far more content for the various pages.

Target Market(s)

Prospective Landlords mainly but tenants also

Industry/Entity Type

Lettings and Property Management

Number of Pages Required

3 page

Font styles to use
Sans Serif
Other font styles liked:
• Candara

Colors
0054AA
0677BA
7BADD7
CADEEF
E8F1F8
F0912C
F2A743
F7CA91
FBE8D2
FDF5EE

Requirements
Must have
• Must be colour co-ordinated to the logo (orange and dark blue predominently, Must have good quality stock images relating to property and renting out property. Should have home page and links to landlord page and tenant page. Must have the 4 logos that we are affiliated to (TKR, Housing Settle, BWN and Tenure Funds Guard) - all attached.
Nice to have
• Modern feel, crisp and sharp but simple - good stock images.

```html
<!DOCTYPE html>
<html lang="en">
<head>
<meta charset="utf-8">
<title>Marlow Vane Lettings</title>
<link rel="stylesheet" href="https://fonts.googleapis.com/css2?family=Cinzel:wght@600;700&family=Roboto:wght@400;500;700&display=swap">
<style>
  :root {
    --navy: #1c3160;
    --orange: #e58714;
    --sky: #0ea7cf;
    --text: #2f2f2f;
    --mist: #f4f4f4;
    --white: #ffffff;
    --badge: #b9b9b9;
  }
  * { box-sizing: border-box; margin: 0; padding: 0; }
  html, body { width: 1059px; height: 1200px; overflow: hidden; }
  body { position: relative; background: var(--white); font-family: "Roboto", sans-serif; color: var(--text); }

  .hero-band { position: absolute; left: 0; top: 0; width: 529px; height: 395px; background: var(--navy); }
  .top-bar { position: absolute; left: 0; top: 0; width: 805px; height: 99px; background: var(--navy); }

  .brand { position: absolute; left: 127px; top: 14px; width: 134px; text-align: center; color: var(--white); font-family: "Cinzel", serif; font-weight: 600; }
  .brand-mark { width: 40px; height: 40px; border-radius: 50%; background: var(--orange); margin: 0 auto 6px; }
  .brand-name { font-size: 15px; line-height: 16px; letter-spacing: .5px; }
  .brand-sub { font-size: 13px; line-height: 16px; letter-spacing: 2px; }
  .brand-tag { font-size: 6px; letter-spacing: 2px; margin-top: 2px; }

  .main-nav { position: absolute; top: 42px; left: 354px; display: flex; gap: 35px; font-weight: 700; font-size: 14px; }
  .main-nav a { color: var(--white); text-decoration: none; }
  .main-nav a.active { color: var(--orange); text-decoration: underline; text-underline-offset: 3px; }
  .nav-divider { position: absolute; left: 641px; top: 27px; width: 1px; height: 46px; background: rgba(255,255,255,.2); }

  .social { display: flex; gap: 3px; }
  .social span { width: 30px; height: 30px; border-radius: 50%; background: var(--white); display: block; }
  .social span:first-child { background: var(--orange); }
  .social.header-social { position: absolute; left: 675px; top: 35px; }

  .enquiry-tab { position: absolute; left: 805px; top: 0; width: 254px; height: 99px; background: var(--orange); color: var(--white); font-weight: 700; font-size: 17px; display: flex; align-items: center; justify-content: center; }

  .hero-title { position: absolute; left: 129px; top: 168px; font-family: "Cinzel", serif; font-weight: 600; font-size: 37px; line-height: 44px; color: var(--white); }
  .hero-photo { position: absolute; left: 529px; top: 99px; width: 530px; height: 353px; background: linear-gradient(135deg, #f3f1ea 0%, #e9e6dc 55%, #d9d2c0 100%); }

  .section-heading { position: absolute; left: 0; width: 1059px; display: flex; justify-content: center; align-items: center; gap: 18px; font-family: "Cinzel", serif; font-weight: 700; font-size: 34px; color: var(--navy); }
  .section-heading::before, .section-heading::after { content: ""; width: 38px; height: 1.5px; background: var(--orange); }
  .story-heading { top: 512px; }

  .story-copy { position: absolute; left: 135px; top: 567px; width: 789px; text-align: center; font-size: 12.7px; line-height: 22px; }
  .story-copy p + p { margin-top: 9px; }

  .cta { position: absolute; left: 450px; top: 745px; width: 159px; height: 39px; border-radius: 3px; background: var(--orange); color: var(--white); font-weight: 700; font-size: 12px; display: flex; align-items: center; justify-content: center; }

  .trusted { position: absolute; left: 0; top: 854px; width: 1059px; height: 268px; background: var(--mist); }
  .trusted-heading { top: 912px; }
  .partner { position: absolute; top: 978px; width: 184px; height: 79px; background: var(--white); border-radius: 6px; box-shadow: 0 2px 4px rgba(0,0,0,.12); display: flex; align-items: center; justify-content: center; }
  .partner-badge { background: var(--badge); border-radius: 4px; }

  .site-footer { position: absolute; left: 0; top: 1122px; width: 1059px; height: 78px; background: var(--sky); }
  .copyright { position: absolute; left: 0; width: 1059px; top: 31px; text-align: center; color: var(--white); font-size: 11px; }
  .social.footer-social { position: absolute; left: 837px; top: 24px; }
</style>
</head>
<body>
  <div class="hero-band"></div>
  <header class="top-bar">
    <div class="brand">
      <div class="brand-mark"></div>
      <div class="brand-name">MARLOW VANE</div>
      <div class="brand-sub">LETTINGS</div>
      <div class="brand-tag">PROPERTY MANAGEMENT</div>
    </div>
    <nav class="main-nav">
      <a class="active" href="#">HOME</a>
      <a href="#">LANDLORDS</a>
      <a href="#">TENANTS</a>
    </nav>
    <div class="nav-divider"></div>
    <div class="social header-social">
      <span aria-label="Social page one"></span><span aria-label="Social page two"></span><span aria-label="Social page three"></span>
    </div>
  </header>
  <div class="enquiry-tab">LANDLORD ENQUIRY</div>

  <h1 class="hero-title">LANDLORDS<br>SUPPORTED.<br>TENANTS VALUED.<br>HOMES ELEVATED.</h1>
  <div class="hero-photo" role="img" aria-label="Photo of a house key resting on a tenancy agreement"></div>

  <h2 class="section-heading story-heading">OUR STORY</h2>
  <div class="story-copy">
    <p>Marlow Vane Lettings has emerged after over 20 years of privately managing our own rental properties.&nbsp; We are family run and decided to move all of our properties under one ‘umbrella’.&nbsp; Now professionally set up as a legal entity, Marlow Vane is looking to welcome new tenants and landlords to an innovative and fresh way of letting property.</p>
    <p>We always maintain a high standard of service and our friendly and helpful team are experienced in all areas and offer an excellent service in helping landlords and tenants deal with problems and issues they face daily.</p>
    <p>Out of hours emergency service which means we are there (in an emergency) for our tenants and landlords 24/7.</p>
  </div>
  <div class="cta">LANDLORD ENQUIRY</div>

  <section class="trusted">
  </section>
  <h2 class="section-heading trusted-heading">TRUSTED BY</h2>
  <div class="partner" style="left:127px"><div class="partner-badge" role="img" aria-label="TKR" style="width:47px;height:51px"></div></div>
  <div class="partner" style="left:334px"><div class="partner-badge" role="img" aria-label="Tenure Funds Guard" style="width:140px;height:28px"></div></div>
  <div class="partner" style="left:541px"><div class="partner-badge" role="img" aria-label="Housing Settle Scheme" style="width:130px;height:36px"></div></div>
  <div class="partner" style="left:748px"><div class="partner-badge" role="img" aria-label="BWN Registered" style="width:59px;height:51px;background:#222"></div></div>

  <footer class="site-footer">
    <div class="copyright">© 2025 &nbsp;/&nbsp; All Rights Reserved</div>
    <div class="social footer-social">
      <span aria-label="Social page one"></span><span aria-label="Social page two"></span><span aria-label="Social page three"></span>
    </div>
  </footer>
</body>
</html>
```